Lindon Business Card

I need a nice and sleek business card.

I need it to promote our website, our rateo page, and or snapgrid page

Snapgrid would be: @lindonjoinery
website would be: www.lindonjoinery-example.com
rateo would be: Lindon Joinery Inc (logo is fine)

Here are a list of service we offer.
1. Custom Kitchen Remodeling
2. Custom Bathroom Remodeling
3. Custom Closet Remodeling
4. Custom Bedroom Remodeling
5. Custom Bars
6. Custom Bookcases
7. Custom Staircases
8. Custom Ceilings

Please use the wording "Every Grain Craft"
We also have been in business since 1992
and we have been serving the rich and famous since.

We do all types of designs, modern and renaissance.

Contact Information for Business Card

Lindon Joinery, Inc.
48715 Brightwell Av,. Unit 305-306
Pacoima, CA. 91331
Telmo Dane Ferucci - CEO
818-555-0143
lindonjoinery@mailbox-example.com

```html
<!DOCTYPE html>
<html lang="en">
<head>
<meta charset="utf-8">
<title>Lindon Joinery Inc. – Business Card</title>
<link rel="stylesheet" href="https://fonts.googleapis.com/css2?family=Cinzel:wght@400;500&family=Crimson+Text:wght@400&display=swap">
<style>
  :root {
    --paper: #ffffff;
    --espresso: #2d1f19;
    --taupe: #8b7c6f;
    --sand: #d3c1aa;
    --ivory: #f1ebe3;
    --crest: #6e5f50;
    --ink: #1f1713;
  }
  * { margin: 0; padding: 0; box-sizing: border-box; }
  html, body {
    width: 1200px; height: 380px; overflow: hidden;
    background: var(--paper);
  }
  .canvas { position: relative; width: 1200px; height: 380px; }

  /* Front */
  .card-front {
    position: absolute; left: 37px; top: 22px;
    width: 525px; height: 299px;
    background: var(--espresso);
  }
  .brand-mark {
    position: absolute; left: 50%; top: 74px;
    width: 124px; height: 124px; margin-left: -62px;
    border-radius: 50%;
    background: radial-gradient(circle, #5a4a3d 0%, #3a2b22 100%);
  }
  .brand-name {
    position: absolute; left: 0; right: 0; top: 202px;
    text-align: center;
    font-family: "Cinzel", serif; font-size: 11px;
    letter-spacing: 3px; color: var(--ivory);
  }
  .web-band {
    position: absolute; left: 0; right: 0; top: 270px; height: 23px;
    background: var(--taupe);
    display: flex; align-items: center; justify-content: center;
    font-family: "Cinzel", serif; font-size: 13px;
    letter-spacing: 1px; color: var(--ivory);
  }

  /* Back */
  .card-back {
    position: absolute; left: 597px; top: 22px;
    width: 525px; height: 299px;
    background: var(--sand);
  }
  .name-band {
    position: absolute; left: 0; right: 0; top: 87px; height: 76px;
    background: var(--paper);
    text-align: center;
  }
  .person-name {
    margin-top: 17px;
    font-family: "Cinzel", serif; font-weight: 400;
    font-size: 24px; line-height: 28px;
    letter-spacing: 1.2px; color: var(--ink);
  }
  .handle {
    font-family: "Cinzel", serif; font-size: 13px; line-height: 16px;
    letter-spacing: 0.8px; color: var(--ink);
  }
  .divider {
    position: absolute; left: 0; right: 0; top: 163px; height: 5px;
    background: var(--espresso);
  }
  .tagline {
    position: absolute; left: 0; right: 0; top: 176px;
    text-align: center;
    font-family: "Crimson Text", serif; font-size: 14px; color: var(--ink);
  }
  .contact {
    position: absolute; left: 0; right: 0; top: 252px;
    text-align: center; font-style: normal;
    font-family: "Crimson Text", serif; font-size: 16px;
    line-height: 22px; color: var(--ink);
  }
</style>
</head>
<body>
<main class="canvas">
  <section class="card-front">
    <div class="brand-mark" role="img" aria-label="Company crest area"></div>
    <p class="brand-name">LINDON JOINERY INC.</p>
    <div class="web-band">WWW.LINDONJOINERY-EXAMPLE.COM</div>
  </section>

  <section class="card-back">
    <div class="name-band">
      <h1 class="person-name">Telmo Dane Ferucci - CEO</h1>
      <p class="handle">@lindonjoinery</p>
    </div>
    <div class="divider"></div>
    <p class="tagline">Every Grain Craft</p>
    <address class="contact">
      48715 Brightwell Av,. Unit 305-306 Halbrook, CA. 9140<br>
      818-555-0143 | lindonjoinery@mailbox-example.com
    </address>
  </section>
</main>
</body>
</html>
```